Brent Oakes Director / Photographer Branding

I need note pads, envelops, business cards and letter head for my company. I'm a fashion and advertising director / photographer. I'm having trouble deciding how to include both Director & Photographer in my title or if it is even necessary. Maybe just my name is enough. I'm open for even using my initials if it works with the design and overall pieces. Please view my website to see what I have at this moment and what work I do. www.brentoakesstudio-mail.net
Updates

Project Deadline Extended
Reason: Hello Everyone! I'm extending the deadline since I have been traveling on a job out of country and I wanted to have more time to look through all the designs and give enough time for everyone to provide changes with designs and updates. I will be more available to communicate online now that I'm back in the office! Thank you! Brent Oakes

Target Market(s)

Fashion magazines, clothing lines and beauty cosmetic brands.

Industry/Entity Type

Fashion Photography

Font styles to use
Sans Serif

Colors
acd036
acd35d
cbcbcb
f5f5f5

Requirements
Must have
• My name.. Brent Oakes, my website: brentoakesstudio-mail.net my phone number, 555-284-6103
• I don't need my address on these. I also live by the philosophy that less is more and keeping things simple ads strength to a design. I also don't want to stop people from taking chances and experimenting with an idea that might take me down different road with my branding.
Nice to have
• Bold designs and clean lines. I'm open to ideas that I could adopt but I lean towards a more minimalistic look in general.
Should not have
• Not have cheesy graphics or pictures. No images of cameras, film or anything that looks like it is a camera or aperture, lens etc... ;)

```html
<!DOCTYPE html>
<html lang="en">
<head>
<meta charset="utf-8">
<title>Brent Oakes – Business Cards</title>
<link rel="stylesheet" href="https://fonts.googleapis.com/css2?family=Jost:wght@300;400&family=Source+Sans+3:wght@400&display=swap">
<style>
  :root {
    --lime: #acd036;
    --ink: #111111;
    --card-black: #0e0e0e;
    --paper: #f5f5f5;
    --backdrop: #cbcbcb;
    --white: #ffffff;
  }
  html, body {
    margin: 0;
    padding: 0;
    width: 1200px;
    height: 900px;
    overflow: hidden;
    background: var(--backdrop);
  }
  .sheet {
    width: 1200px;
    height: 900px;
    display: flex;
    align-items: center;
    justify-content: center;
    gap: 90px;
  }
  .card {
    position: relative;
    width: 330px;
    height: 578px;
    box-sizing: border-box;
    border-right: 3px solid var(--lime);
  }
  .card--front {
    background: var(--card-black);
  }
  .card--back {
    background: var(--paper);
  }
  .vertical {
    position: absolute;
    writing-mode: vertical-rl;
    margin: 0;
  }
  .title-line {
    top: 26px;
    right: 26px;
    font-family: "Source Sans 3", sans-serif;
    font-size: 14px;
    letter-spacing: 0.2px;
    color: var(--white);
  }
  .name {
    font-family: "Jost", sans-serif;
    font-weight: 300;
    font-size: 50px;
    line-height: 1;
    letter-spacing: 1px;
    text-transform: uppercase;
  }
  .name--front {
    bottom: 36px;
    right: 30px;
    color: var(--lime);
  }
  .name--back {
    top: 34px;
    right: 74px;
    color: var(--ink);
    transform: rotate(180deg);
  }
  .contact {
    position: absolute;
    left: 32px;
    bottom: 34px;
    margin: 0;
    font-family: "Source Sans 3", sans-serif;
    font-size: 15px;
    line-height: 1.3;
    color: var(--ink);
  }
  .contact__role {
    display: block;
    margin-bottom: 14px;
  }
  .contact__web,
  .contact__phone {
    display: block;
  }
</style>
</head>
<body>
  <main class="sheet">
    <section class="card card--front" aria-label="Business card front">
      <p class="vertical title-line">Director &amp; Photographer</p>
      <h1 class="vertical name name--front">Brent<br>Oakes</h1>
    </section>
    <section class="card card--back" aria-label="Business card back">
      <h2 class="vertical name name--back">Brent<br>Oakes</h2>
      <p class="contact">
        <span class="contact__role">Director &amp; Photographer</span>
        <span class="contact__web">brentoakesstudio-mail.net</span>
        <span class="contact__phone">555-284-6103</span>
      </p>
    </section>
  </main>
</body>
</html>
```